Flyer Design Project for The Verdance Studio

I'm a Naturopathic Herbalist who wishes to expand my business from x1 a week to x5 days a week and so need to produce a flyer to let people know what I do and to guide them to my website at theverdancestudio.com.au.
One-sided or double-sided A5 flyer on good quality paper for distribution by my referral network.  If all the info can fit on one side that would be great.
It would be great if the design could link up with my website i.e. the sun, mountains etc in the background but don't worry if not possible so then as an alternative I'd like to see something modern, fresh.
Otherwise it's to be simple, clean, easy to read, with a couple of relevant pictures if you want.

Target Market(s)
Predominantly females, from teens "clear skin tonics" to overloaded twenty-somethings, to pre-baby fertility programmes, healthy pregnancy etc
Industry/Entity Type
Business
Look and feel

```html
<!DOCTYPE html>
<html lang="en">
<head>
<meta charset="utf-8">
<title>Sick and Tired? Herbal Medicine Flyer – The Verdance Studio</title>
<link rel="stylesheet" href="https://fonts.googleapis.com/css2?family=Roboto:wght@100;300;400;500&family=Archivo+Black&family=Arimo:wght@400;700&display=swap">
<style>
  :root {
    --magenta: #e8288a;
    --paper-grey: #e8e8e8;
    --white: #ffffff;
    --ink: #4a4a4a;
    --basil-dark: #5a1a1c;
    --basil-mid: #9a3638;
  }
  * { margin: 0; padding: 0; box-sizing: border-box; }
  html, body { width: 1200px; height: 852px; overflow: hidden; background: var(--paper-grey); }
  .flyer { position: relative; width: 1200px; height: 852px; background: var(--paper-grey); font-family: "Arimo", Arial, sans-serif; }

  /* Left panel */
  .hero { position: absolute; left: 0; top: 0; width: 600px; height: 852px; background: var(--magenta); overflow: hidden; color: var(--white); }
  .hero__mark { position: absolute; left: 370px; top: 120px; font-family: "Roboto", Arial, sans-serif; font-weight: 500; font-size: 440px; line-height: 1; }
  .hero__sick { position: absolute; left: 134px; top: 282px; font-family: "Roboto", Arial, sans-serif; font-weight: 100; font-size: 128px; line-height: 1; letter-spacing: -2px; }
  .hero__and { position: absolute; left: 214px; top: 418px; font-family: "Roboto", Arial, sans-serif; font-weight: 300; font-size: 70px; line-height: 1; }
  .hero__tired { position: absolute; left: 54px; top: 440px; font-family: "Archivo Black", "Arial Black", sans-serif; font-size: 158px; line-height: 1; letter-spacing: -6px; }
  .hero__tagline { position: absolute; left: 90px; top: 580px; font-family: "Roboto", Arial, sans-serif; font-weight: 300; font-size: 25.5px; line-height: 24px; text-transform: uppercase; letter-spacing: 0.2px; }
  .hero__leaf { position: absolute; left: 185px; top: 625px; width: 180px; height: 200px; }

  /* Right panel copy */
  .copy { position: absolute; top: 57px; width: 231px; font-size: 12.6px; line-height: 23.5px; color: var(--ink); text-align: justify; }
  .copy p { margin-bottom: 23.5px; }
  .copy--left { left: 653px; }
  .copy--right { left: 917px; }
  .copy .compact { line-height: 16px; margin-bottom: 24px; }
  .copy .link { color: var(--magenta); font-weight: 700; }

  /* Contact card */
  .contact { position: absolute; left: 718px; top: 656px; width: 365px; height: 138px; }
  .contact__shape { position: absolute; inset: 0; }
  .contact__text { position: absolute; left: 0; top: 33px; width: 100%; text-align: center; font-size: 13.2px; line-height: 16.5px; color: var(--ink); }
  .contact__name { color: var(--magenta); font-weight: 700; font-size: 15.5px; line-height: 20px; }
</style>
</head>
<body>
<main class="flyer">
  <section class="hero">
    <div class="hero__mark" aria-hidden="true">?</div>
    <div class="hero__sick">Sick</div>
    <div class="hero__and">and</div>
    <div class="hero__tired">Tired</div>
    <p class="hero__tagline">Herbal medicine could<br>be the answer for you.</p>
    <svg class="hero__leaf" viewBox="0 0 180 200" role="img" aria-label="Photograph of fresh red basil leaves">
      <defs>
        <radialGradient id="basil" cx="45%" cy="45%" r="60%">
          <stop offset="0" stop-color="var(--basil-mid)"/>
          <stop offset="1" stop-color="var(--basil-dark)"/>
        </radialGradient>
      </defs>
      <ellipse cx="90" cy="105" rx="85" ry="90" fill="url(#basil)" opacity="0.85"/>
    </svg>
  </section>

  <div class="copy copy--left">
    <p>Maren has a wealth of experience with over 14 years in clinical practice which, coupled with a great deal of “life experience” as the mother of three children, helps to make your consultation professional, caring and healing.</p>
    <p>Passionate about helping you reach your highest potential health-wise, Maren will make you a “Daily Wellness Tonic” which is like the best multi-vitamin you could have as it’s tailor-made especially for you. The “Daily Wellness Tonic” can help strengthen, nourish, heal and rebalance your whole body.</p>
    <p>“Daily Wellness Tonics” can be made to assist you keeping yourself well, for nurturing yourself (so in turn you can nurture others), for re-energising you, for aging gracefully, to assist you feeling back on top of life and to help you face challenges more easily.</p>
  </div>

  <div class="copy copy--right">
    <p>Herbal medicine can help with Sleep Disorders, Weak Immune Systems, Anxiety, Depression, Fertility issues, Childhood Diseases, Skin Problems, Gastro-Intestinal Disorders and Women’s Health.</p>
    <p>Maren also specialises in “Super Immune Boost Tonics” assisting with acute conditions such as coughs, colds, sore throats and offers 20-30 minute “Express Appointments”. Useful as a preventative measure or as a way of healing these conditions more quickly.</p>
    <p class="compact">“Clear Skin Wellness Tonics” are popular with teens and a special teen package is also offered as an “Express Appointment” with a bottle of tonic.</p>
    <p class="compact">For more information, check out The Verdance Studio website at <span class="link">www.theverdancestudio.com.au</span></p>
  </div>

  <div class="contact">
    <svg class="contact__shape" viewBox="0 0 365 138" aria-hidden="true">
      <rect x="85" y="0" width="96" height="30" fill="var(--white)"/>
      <rect x="0" y="20" width="365" height="90" fill="var(--white)"/>
      <rect x="94" y="100" width="144" height="38" fill="var(--white)"/>
    </svg>
    <div class="contact__text">
      <div class="contact__name">Maren Holt DHM,</div>
      Local Naturopathic Herbalist<br>
      joins the professional team at Willow Grove Clinic<br>
      48 Fernleigh Road, Ashwood, NSW, 2099<br>
      Ph: 0491 570 156
    </div>
  </div>
</main>
</body>
</html>
```